Poster Design for Photography Exhibit

We are looking for a poster design for a photography exhibit featuring high-end fashion and celebrity photography.

Name of the exhibit is "MILES DORVAN: UNTITLED" (please use Helvetica Black all cap for show name.

Poster is LANDSCAPE format (2 units wide by 1 unit high).

Unfortunately due to legal reasons, we cannot use any actual Miles Dorvan photos. No can we use fashions or people on the poster!

We are looking for a high-end, sexy, bold provocative design that captures the excitement and glamour of a fashion photo shoot.

Target Market(s)

Men and Women interested in Fashion Photography and art photography in general

Industry/Entity Type

Fashion

Requirements
Must have
• landscape format, name of exhibit in Helvetica Black all caps
Nice to have
• Can be grayscale or color.
Should not have
• Logos or brand names

```html
<!DOCTYPE html>
<html lang="en">
<head>
<meta charset="UTF-8">
<title>Miles Dorvan : Untitled — Exhibition Poster</title>
<link rel="stylesheet" href="https://fonts.googleapis.com/css2?family=Archivo+Black&display=swap">
<style>
  :root {
    --stage: #000000;
    --paper: #ffffff;
    --warm-deep: #e8621a;
    --warm-mid: #f19a4e;
    --warm-soft: #f6cf9f;
    --cream: #f3f0dd;
    --ground: #dfe2c6;
    --rule: #3a3a32;
    --name-start: #f28a2c;
    --name-end: #d8a640;
    --title-olive: #6e7b3c;
  }
  * { margin: 0; padding: 0; box-sizing: border-box; }
  html, body {
    width: 1200px;
    height: 900px;
    overflow: hidden;
    background: var(--stage);
  }
  .poster {
    position: absolute;
    left: 44px;
    top: 173px;
    width: 1113px;
    height: 555px;
    background: var(--paper);
    overflow: hidden;
  }
  .poster__photo {
    position: absolute;
    inset: 0;
    background:
      linear-gradient(90deg,
        rgba(255,255,255,0) 0%,
        rgba(255,255,255,0) 38%,
        rgba(255,255,255,0.85) 68%,
        var(--paper) 86%),
      linear-gradient(180deg,
        var(--warm-soft) 0%,
        var(--warm-mid) 20%,
        var(--warm-soft) 55%,
        var(--cream) 74%,
        var(--ground) 100%),
      linear-gradient(90deg,
        var(--warm-deep) 0%,
        var(--warm-mid) 30%,
        var(--cream) 60%);
    background-blend-mode: normal, multiply, normal;
  }
  .poster__band {
    position: absolute;
    left: 0;
    right: 0;
    top: 207px;
    height: 105px;
    background: var(--paper);
    border-top: 1px solid var(--rule);
    border-bottom: 1px solid var(--rule);
    display: flex;
    align-items: center;
    padding-left: 82px;
  }
  .show-title {
    font-family: "Archivo Black", "Helvetica Neue", Arial, sans-serif;
    font-weight: 400;
    font-size: 55px;
    line-height: 1;
    letter-spacing: 0.5px;
    text-transform: uppercase;
    white-space: nowrap;
  }
  .show-title__artist {
    background: linear-gradient(90deg, var(--name-start), var(--name-end));
    -webkit-background-clip: text;
    background-clip: text;
    color: transparent;
  }
  .show-title__work {
    color: var(--title-olive);
  }
</style>
</head>
<body>
  <main class="poster">
    <div class="poster__photo" role="img" aria-label="Warm orange-toned photograph of a seated figure on a chair against a brick wall, fading to white on the right"></div>
    <div class="poster__band">
      <h1 class="show-title">
        <span class="show-title__artist">Miles Dorvan : </span><span class="show-title__work">Untitled</span>
      </h1>
    </div>
  </main>
</body>
</html>
```